Beer Sommelier Business Card

Dear Designers,
I'm looking forward a Beer Sommelier business card. I'm a Beer Sommelier and also a Chef in Rio de Janeiro, Brazil but this card has to be a Beer Sommelier card.
I do consulting, brigade training, tastings and harmonizations.
Forget about themes such as rock and roll, motorcycles, conventional English pubs and bellied beer drinkers. This business card will be delivered to restaurant owners and investors in Rio.
It has to seek elegance rather than luxury, and refinement rather than fashion.
I work using a black dress shirt, a Varnel Osterby watch and a 18k 1981 Dumelle aviator eyeglasses. I'm a business man and It's all part of the game.
Obviously, it has to be written in PORTUGUESE (only) and just as little as possible.

Informations to be included:

Tiago Varquim

Beer Sommelier
Chef de Cuisine

Consultoria
Treinamento de Brigada
Degustações
Harmonizações

telephone number (just numbers): 947261380

email (just the adress): tiagovarquim@mailnest.example

PS:
The letter "c" on both words "Degustações" and "Harmonizações" they have a small trace under it.
The letter "o" on both words "Degustações" and "Harmonizações" they have a small wave above it.

Blame the Latin.

Best Regards

Target Market(s)

Restaurant Owners and Investors. I have to impress them with my business card before I offer my services.

Industry/Entity Type

Restaurant

Contact Information for Business Card

An unique and well constructed Sommelier Business Card

Requirements
Must have
• A firts look impact. An unique and well made design. Not an ordinary product.
• Tiago Varquim
• Beer Sommelier/Chef de Cuisine
• Consultoria
• Treinamento de Brigada
• Degustações
• Harmonizações
• telephone number (just numbers): 947261380
• email (just the adress): tiagovarquim@mailnest.example
• PS:
• The letter "c" on both words "Degustações" and "Harmonizações" they have a small trace under it.
• The letter "o" on both words "Degustações" and "Harmonizações" they have a small wave above it.
Nice to have
• Elegance, Refinement.
• Should be a Pro Style good Looking card,
• Forget themes like beer, chef and cuisine,
• It could be a laser engraved, metal, stainless steel, PVC, Triplex, Smooth, Letterpress, all black or any other good idea.
Should not have
• Words like telephone, email, cartoon pics or glass pics.
• Should not be an ordinary card that I could download from the web or use a web program and easily make by my self.
• Just Portuguese words

```html
<!DOCTYPE html>
<html lang="pt">
<head>
<meta charset="utf-8">
<title>Tiago Varquim — Beer Sommelier</title>
<link rel="stylesheet" href="https://fonts.googleapis.com/css2?family=Pinyon+Script&family=Roboto:wght@400&display=swap">
<style>
  :root {
    --page: #e9e4dc;
    --wood-dark: #2a1a12;
    --wood-mid: #5a3a26;
    --wood-light: #8a6446;
    --amber-deep: #9a5a24;
    --amber: #c98a3e;
    --band: rgba(245, 243, 240, 0.88);
    --ink: #3b3633;
    --ink-soft: #5c5754;
    --white: #ffffff;
  }
  * { box-sizing: border-box; margin: 0; padding: 0; }
  html, body { width: 1200px; height: 1000px; overflow: hidden; }
  body {
    background: var(--page);
    position: relative;
    font-family: "Roboto", Arial, sans-serif;
  }
  .card {
    position: absolute;
    width: 560px;
    height: 330px;
    overflow: hidden;
    border-radius: 4px;
    box-shadow: 0 10px 30px rgba(0,0,0,0.25);
  }
  .card--front { left: 90px; top: 110px; }
  .card--back { left: 550px; top: 560px; }

  .card__backdrop {
    position: absolute; inset: 0;
    background:
      radial-gradient(ellipse at 60% 55%, var(--wood-light) 0%, transparent 55%),
      linear-gradient(135deg, var(--wood-dark) 0%, var(--wood-mid) 55%, var(--wood-dark) 100%);
  }
  .card__photo {
    position: absolute;
    background: linear-gradient(160deg, var(--amber) 0%, var(--amber-deep) 100%);
  }
  .card--front .card__photo { left: 130px; right: 0; top: 0; height: 130px; }
  .card--back .card__photo { left: 130px; right: 0; bottom: 0; height: 100px; }

  .card__band {
    position: absolute;
    left: 0; right: 0;
    background: var(--band);
  }
  .card--front .card__band { top: 140px; height: 110px; padding: 10px 0 0 36px; }
  .card--back .card__band { top: 84px; height: 136px; width: 380px; padding: 18px 0 0 32px; }

  .name {
    font-family: "Pinyon Script", cursive;
    font-weight: 400;
    font-size: 58px;
    line-height: 1;
    color: var(--ink);
  }
  .role {
    font-family: "Pinyon Script", cursive;
    font-size: 22px;
    color: var(--ink-soft);
    margin: 8px 0 0 76px;
  }
  .role__divider { padding: 0 6px; font-family: "Roboto", Arial, sans-serif; font-size: 18px; }

  .contact {
    position: absolute;
    left: 36px; bottom: 16px;
    color: var(--white);
    font-size: 17px;
    line-height: 1.35;
    list-style: none;
  }

  .services-title {
    position: absolute;
    right: 24px; top: 12px;
    font-family: "Pinyon Script", cursive;
    font-weight: 400;
    font-size: 60px;
    line-height: 1;
    color: var(--white);
  }
  .services {
    list-style: none;
    color: var(--ink);
    font-size: 19px;
    line-height: 1.38;
  }
</style>
</head>
<body>

  <section class="card card--front" aria-label="Frente do cartão">
    <div class="card__backdrop" role="img" aria-label="Fotografia de fundo em tons de madeira escura"></div>
    <div class="card__photo" role="img" aria-label="Fotografia de uma taça de cerveja"></div>
    <div class="card__band">
      <h1 class="name">Tiago Varquim</h1>
      <p class="role">Beer Sommelier<span class="role__divider">|</span>Chef de Cuisine</p>
    </div>
    <ul class="contact">
      <li>947261380</li>
      <li>tiagovarquim@mailnest.example</li>
    </ul>
  </section>

  <section class="card card--back" aria-label="Verso do cartão">
    <div class="card__backdrop" role="img" aria-label="Fotografia de fundo em tons de madeira escura"></div>
    <div class="card__photo" role="img" aria-label="Fotografia de uma taça de cerveja"></div>
    <h2 class="services-title">Serviços</h2>
    <div class="card__band">
      <ul class="services">
        <li>Consultoria</li>
        <li>Treinamento de Brigada</li>
        <li>Degustações</li>
        <li>Harmonizações</li>
      </ul>
    </div>
  </section>

</body>
</html>
```